R&T Promotions / P.L.W. Sales Business Cards

I have 2 companies that are somewhat connected, yet sell to 2 different markets.

R&T Promotions www.rotapfx.example

We are a manufacturers representative company. We handle sales and marketing of Home Theater, Home Automation, Audio & Video products for the state of Florida. We work with Designers, Architects, Technology Consultants and Electronic Integrators to design, sell and install cutting edge technology in new and existing homes, condos and commercial spaces.

P.L.W. Sales www.plwqz.example

We are a manufacturers representative company. We handle sales and marketing of automotive Audio, Electronics, Security, Navigation and Entertainment products for the state of Florida. We work with 12-volt retailers, installers and automobile customizers to design, sell, merchandise, fabricate and install cutting edge technology in cars, boats, motor coaches, etc.

We have logo's that might still be relevant, but might need a little touching up. We need a new business card design and layout for each of the 2 companies. I would like them to have a family look, but still better speak to the customer base associated with the channel.

Target Market(s)

R&T Promotions -

Design, Engineering, Construction, Technology, elegant, tasteful.

P.L.W. Sales -

More cutting edge, industrial, youth, aggressive, fun, bold.

Industry/Entity Type

Business

Requirements
Must have
• New business card layout for both companies.
Nice to have
• A family look, or relationship to the other company. Even if it's just a logo referencing the other company.

```html
<!DOCTYPE html>
<html lang="en">
<head>
<meta charset="utf-8">
<title>P.L.W. Sales Business Card</title>
<link rel="stylesheet" href="https://fonts.googleapis.com/css2?family=Roboto:wght@300;400;700&display=swap">
<style>
  :root {
    --paper: #ffffff;
    --ink: #111111;
    --ink-soft: #5a5a5a;
    --band-top: #3c4a63;
    --band-plum: #5b4c5e;
    --band-mid: #b8502a;
    --band-warm: #e0701c;
    --band-low: #f3a51e;
    --mark: #ffffff;
  }
  * { box-sizing: border-box; margin: 0; padding: 0; }
  html, body {
    width: 1200px;
    height: 694px;
    overflow: hidden;
    background: var(--paper);
  }
  .card {
    position: relative;
    width: 1200px;
    height: 694px;
    background: var(--paper);
    font-family: "Roboto", "Helvetica Neue", Arial, sans-serif;
    color: var(--ink);
  }
  .brand-band {
    position: absolute;
    left: 0;
    top: 0;
    width: 436px;
    height: 694px;
    overflow: hidden;
  }
  .brand-band-backdrop {
    position: absolute;
    inset: 0;
    background: linear-gradient(172deg,
      var(--band-top) 0%,
      var(--band-plum) 22%,
      var(--band-mid) 48%,
      var(--band-warm) 70%,
      var(--band-low) 100%);
  }
  .company-name {
    position: absolute;
    left: 100px;
    top: 76px;
    color: var(--mark);
    font-weight: 700;
    font-size: 50px;
    line-height: 54px;
    letter-spacing: 1px;
  }
  .sister-company {
    position: absolute;
    left: 58px;
    top: 556px;
    display: flex;
    align-items: center;
    gap: 10px;
    color: var(--mark);
    font-weight: 700;
    font-size: 19px;
    line-height: 22px;
  }
  .sister-company .dot {
    width: 18px;
    height: 18px;
    border-radius: 50%;
    background: var(--mark);
    flex: none;
  }
  .partner-badge {
    position: absolute;
    left: 258px;
    top: 538px;
    width: 124px;
    height: 86px;
    border-radius: 10px;
    background: var(--mark);
  }
  .identity {
    position: absolute;
    right: 68px;
    top: 52px;
    text-align: right;
  }
  .identity .person {
    font-weight: 300;
    font-size: 56px;
    line-height: 64px;
    letter-spacing: -0.5px;
  }
  .identity .role {
    font-weight: 300;
    font-size: 31px;
    line-height: 36px;
    color: var(--ink-soft);
  }
  .contact {
    position: absolute;
    right: 58px;
    top: 384px;
    text-align: right;
    font-weight: 400;
    font-size: 25px;
    line-height: 39px;
    font-style: normal;
  }
</style>
</head>
<body>
  <div class="card">
    <div class="brand-band">
      <div class="brand-band-backdrop" role="img" aria-label="Warm abstract light-streak background in slate blue, rust and amber"></div>
      <div class="company-name">P.L.W.<br>Sales</div>
      <div class="sister-company"><span class="dot"></span>R&amp;T<br>Promotions</div>
      <div class="partner-badge"></div>
    </div>

    <div class="identity">
      <div class="person">Daniel Korvath</div>
      <div class="role">Rep Principle</div>
    </div>

    <address class="contact">
      4417 Ridgeline Avenue<br>
      Tallow, FL 30199<br>
      tel: 800-555-0142<br>
      cell: 555-201-4470<br>
      fax: 555-301-7721<br>
      daniel@plwqz.example<br>
      http://www.plwqz.example
    </address>
  </div>
</body>
</html>
```